Web Design - Outdoor Equipment, Ultra-High Durability

The task is to provide us with a new web design for our danish company, producing outdoor equipment such as backpacks and clothing with ultra high durability, and performance. Our main concept is a design/web page showing some of the very extreme quality tests of our products - (video/image), and with a integrated online shop. We use only the best and most toughest materials in our production of equipment.

We are looking for a web design with colors and theme that should resemble the outdoor/nature/cold climate combined with the high quality products of the company. We focus on a slightly more modern design/concept, towards the extreme sport segment. It is important that the design fits our logo, and combine the modern features with the "durability of old equipment".

Keywords: Unique, Recognizable, Outdoor, High Quality.

Another key feature is the combination of our existing company logo which represent the company strengths. See attached images. We would further more like to extend some of the web design to our business cards if possible. Color changes accepted.

Our company name "Brambleton" is part of the logo, but could be combined otherwise. We are looking forward to cooperate with the winner in the future.

Be creative - now is the chance!

Target Market(s)

Outdoor, Ultra-High Durability, High Quality, Fishing, Climbing, Extreme Sports.

Industry/Entity Type

Business

Requirements
Must have
• Strength, but not heavy appearance. Online shop feature.
Nice to have
• Polar Bear Logo, Mountains, Trekking, Cold Climate Elements or Colors etc. (Help with the setup of the page, shop etc.) Small Danish Flag

```html
<!DOCTYPE html>
<html lang="en">
<head>
<meta charset="utf-8">
<title>Brambleton Adventure Equipment</title>
<link rel="stylesheet" href="https://fonts.googleapis.com/css2?family=Oswald:wght@400;500;600&family=Roboto:wght@400;500;700&display=swap">
<style>
:root{
  --red:#c8141b;
  --red-dark:#a10f14;
  --ink:#1f2227;
  --nav:#2b2f35;
  --nav-dark:#1e2126;
  --text:#3a3d42;
  --muted:#6c7076;
  --panel:#e4e8ec;
  --line:#b9bec4;
  --star:#e07a10;
  --snow:#eef3f8;
}
*{box-sizing:border-box;margin:0;padding:0}
html,body{width:771px;height:1200px;overflow:hidden}
body{font-family:"Roboto",Arial,sans-serif;color:var(--text);background:var(--snow);position:relative}
.backdrop{position:absolute;left:0;top:0;width:771px;height:1200px;
  background:linear-gradient(180deg,#dfe8f1 0%,#eef3f8 30%,#f5f8fb 60%,#f7f9fb 100%)}
.abs{position:absolute}
.brand{left:59px;top:18px;display:flex;align-items:center;gap:5px}
.brand-square{width:18px;height:18px;background:var(--ink)}
.brand-name{font-family:"Oswald",sans-serif;font-weight:600;font-size:22px;color:var(--red);letter-spacing:.5px;line-height:1}
.phone{right:61px;top:26px;font-size:12.5px;font-weight:500;color:var(--ink)}
.phone span{color:var(--red)}
.nav{left:59px;top:69px;width:652px;height:38px;background:linear-gradient(180deg,#363b42,var(--nav));display:flex;align-items:center;
  box-shadow:0 0 0 4px rgba(255,255,255,.6)}
.nav a{color:#fff;text-decoration:none;font-size:10.5px;font-weight:500;height:38px;display:flex;align-items:center;justify-content:center;border-right:1px solid #23262b}
.nav .mark{background:var(--nav-dark);width:64px}
.hero{left:59px;top:113px;width:652px;height:283px;
  background:radial-gradient(ellipse at 82% 45%,#c9252a 0,#c9252a 12%,transparent 30%),
  linear-gradient(170deg,#2b61b8 0%,#4f86d4 35%,#dfe8f3 60%,#ffffff 80%,#cfd9e6 100%)}
.dots{left:81px;top:258px;display:flex;gap:3px}
.dots i{width:9px;height:9px;border:1.5px solid #fff;border-radius:50%;display:block}
.hero-title{left:79px;top:276px;font-family:"Oswald",sans-serif;font-size:28px;line-height:31px;color:#fff;font-weight:500;letter-spacing:-.5px}
.hero-title .dark{color:var(--ink)}
.hero-text{left:79px;top:344px;width:350px;font-size:11.5px;line-height:16px;color:#2d3035}
.card{top:402px;width:213px;height:117px;color:#fff}
.card-img{position:absolute;inset:0}
.card .kicker{position:absolute;left:10px;top:44px;font-family:"Oswald",sans-serif;font-size:13px;color:#111}
.card .label{position:absolute;left:10px;top:61px;background:var(--red);font-family:"Roboto",sans-serif;font-weight:700;font-size:13.5px;padding:1px 3px;line-height:16px}
.card .desc{position:absolute;left:10px;top:83px;font-size:8.5px;line-height:12px;width:150px}
.sec-head{left:59px;top:539px;width:652px;height:24px;border-bottom:2px dotted var(--line)}
.sec-head h2{font-weight:400;font-size:12.5px;color:var(--ink)}
.sec-head h2 b{color:var(--red);font-weight:500}
.sec-head .all{position:absolute;right:0;top:3px;font-size:8px;color:var(--ink)}
.arrow{top:638px;width:0;height:0;border-top:6px solid transparent;border-bottom:6px solid transparent}
.product{top:585px;width:215px;height:130px}
.product h3{position:absolute;left:6px;top:6px;font-size:10.5px;font-weight:500;color:var(--ink)}
.product p{position:absolute;left:6px;top:27px;width:120px;font-size:8px;line-height:12px;color:var(--muted)}
.product .price{position:absolute;left:6px;top:76px;font-size:13.5px;font-weight:500;color:var(--red)}
.product .stars{position:absolute;left:70px;top:79px;font-size:8.5px;letter-spacing:1px;color:#c4c7cb}
.product .stars b{color:var(--star);font-weight:400}
.product .cart{position:absolute;left:6px;top:105px;height:15px;display:flex;font-size:7px;font-weight:700;color:#fff}
.cart .ic{width:20px;background:var(--red);display:flex;align-items:center;justify-content:center}
.cart .tx{background:var(--ink);padding:0 6px;display:flex;align-items:center}
.product .details{position:absolute;left:92px;top:108px;font-size:7px;font-weight:500;color:var(--ink)}
.product .pimg{position:absolute;left:146px;top:0;width:64px;height:128px;border-radius:24px 24px 12px 12px;
  background:linear-gradient(180deg,#6d7f90 0%,#6d7f90 18%,#d92a25 30%,#c01e1c 75%,#4d5864 100%)}
.info{left:53px;top:742px;width:664px;height:211px;background:linear-gradient(180deg,#eceff2,#dfe3e7);box-shadow:0 -3px 5px rgba(0,0,0,.12)}
.info-col{top:20px;width:300px;height:180px}
.info-col h2{font-family:"Oswald",sans-serif;font-weight:500;font-size:16.5px;color:var(--red);letter-spacing:.3px}
.info-col h4{font-size:10px;font-weight:500;color:var(--ink);margin-top:1px}
.info-col p{position:absolute;top:62px;width:180px;font-size:8.6px;line-height:12px;color:#555a60}
.info-col .more{position:absolute;top:145px;background:var(--ink);color:#fff;font-size:6.8px;font-weight:700;padding:3px 10px}
.info-col .circle{position:absolute;left:200px;top:43px;width:93px;height:93px;border-radius:50%;box-shadow:0 2px 5px rgba(0,0,0,.25)}
.news{left:53px;top:959px;width:664px;height:45px;background:linear-gradient(105deg,var(--red) 0,var(--red-dark) 40%,#2a2e34 40.3%,#3b4047 100%)}
.news h3{position:absolute;left:12px;top:7px;font-family:"Oswald",sans-serif;font-weight:500;font-size:13px;color:#fff}
.news p{position:absolute;left:12px;top:26px;font-size:8px;color:#fff}
.news .field{position:absolute;left:414px;top:13px;width:198px;height:20px;background:#fff;border:1px solid #ccc;font-size:8px;color:#888;padding:5px 8px}
.news .submit{position:absolute;left:612px;top:13px;width:38px;height:20px;background:var(--red);color:#fff;font-size:8.5px;display:flex;align-items:center;justify-content:center}
.foot-rule{left:51px;top:1046px;width:669px;border-top:2px dotted var(--line)}
.foot-square{left:366px;top:1034px;width:26px;height:26px;background:#fff;border:2px solid var(--line)}
.foot-col{top:1076px}
.foot-col h5{font-family:"Oswald",sans-serif;font-weight:500;font-size:11px;color:var(--red);margin-bottom:6px}
.foot-col a{display:block;font-size:8.3px;color:var(--ink);text-decoration:none;line-height:14.6px}
.world{left:478px;top:1062px;width:244px;height:114px;border-radius:40px;
  background:radial-gradient(ellipse at center,#d4d9de 0,#e4e8ec 55%,transparent 75%)}
.foot-brand{left:519px;top:1101px;display:flex;align-items:center;gap:5px}
</style>
</head>
<body>
<div class="backdrop" role="img" aria-label="Snowy mountain peaks under a pale winter sky"></div>

<header>
  <div class="abs brand"><span class="brand-square"></span><span class="brand-name">BRAMBLETON</span></div>
  <div class="abs phone">Call us now <span>555 019 284</span></div>
  <nav class="abs nav">
    <a style="width:70px">HOME</a>
    <a style="width:90px">ABOUT US</a>
    <a style="width:132px">OUR PRODUCTS</a>
    <a class="mark" aria-label="Home"></a>
    <a style="width:136px">OUR SERVICES</a>
    <a style="width:70px">SHOP</a>
    <a style="width:90px;border-right:0">CONTACT</a>
  </nav>
</header>

<section class="abs hero" role="img" aria-label="Climber on a snowy ridge with a red trekking backpack in the foreground"></section>
<div class="abs dots"><i></i><i></i><i></i><i></i><i></i></div>
<h1 class="abs hero-title">BACKPACKS FOR EVERY<br><span class="dark">ADVENTURE</span></h1>
<p class="abs hero-text">Lorem ipsum dolor sit amet, consectetur adipiscing elit. Nulla convallis placerat nulla, non eleifend neque scelerisque et.</p>

<a class="abs card" style="left:59px">
  <div class="card-img" role="img" aria-label="Blue trekking backpack in front of snowy mountains" style="background:linear-gradient(160deg,#5b8fd0 0%,#c9d9ec 45%,#3a6fb0 75%,#1e4f8e 100%)"></div>
  <span class="kicker">Shop</span><span class="label">BACKPACKS</span>
  <span class="desc">Lorem ipsum dolor sit amet, consectetur adipiscing</span>
</a>
<a class="abs card" style="left:278px">
  <div class="card-img" role="img" aria-label="Blue and black outdoor jackets against a mountain landscape" style="background:linear-gradient(160deg,#3c6cb8 0%,#bfd0e4 40%,#1f8ad8 70%,#23262b 100%)"></div>
  <span class="kicker">Shop</span><span class="label">CLOTHING</span>
  <span class="desc">Lorem ipsum dolor sit amet, consectetur adipiscing</span>
</a>
<a class="abs card" style="left:498px">
  <div class="card-img" role="img" aria-label="Ski boots in front of a ski lift" style="background:linear-gradient(160deg,#2d5aa8 0%,#6f97cf 40%,#c8ced6 70%,#4b4f57 100%)"></div>
  <span class="kicker">Shop</span><span class="label">EQUIPMENT</span>
  <span class="desc">Lorem ipsum dolor sit amet, consectetur adipiscing</span>
</a>

<div class="abs sec-head"><h2>FEATURED <b>PRODUCTS</b></h2><span class="all">see all products</span></div>
<span class="abs arrow" style="left:48px;border-right:5px solid var(--red)"></span>
<span class="abs arrow" style="left:718px;border-left:5px solid var(--red)"></span>

<article class="abs product" style="left:59px">
  <h3>Ultra High red Backpack</h3>
  <p>Lorem ipsum dolor sit amet, consectetur adipiscing elitt. Maecenas eleifend metus...</p>
  <span class="price">€350.22</span><span class="stars"><b>★★</b>★★★</span>
  <span class="cart"><span class="ic"><svg width="9" height="8" viewBox="0 0 9 8"><path d="M0 1h2l1 4h5l1-3H3" fill="none" stroke="#fff" stroke-width="1"/><circle cx="3.5" cy="7" r=".8" fill="#fff"/><circle cx="7" cy="7" r=".8" fill="#fff"/></svg></span><span class="tx">add to cart</span></span>
  <span class="details">details</span>
  <div class="pimg" role="img" aria-label="Red trekking backpack"></div>
</article>
<article class="abs product" style="left:280px">
  <h3>Ultra High red Backpack</h3>
  <p>Lorem ipsum dolor sit amet, consectetur adipiscing elitt. Maecenas eleifend metus...</p>
  <span class="price">€350.22</span><span class="stars"><b>★★</b>★★★</span>
  <span class="cart"><span class="ic"><svg width="9" height="8" viewBox="0 0 9 8"><path d="M0 1h2l1 4h5l1-3H3" fill="none" stroke="#fff" stroke-width="1"/><circle cx="3.5" cy="7" r=".8" fill="#fff"/><circle cx="7" cy="7" r=".8" fill="#fff"/></svg></span><span class="tx">add to cart</span></span>
  <span class="details">details</span>
  <div class="pimg" role="img" aria-label="Red trekking backpack"></div>
</article>
<article class="abs product" style="left:500px">
  <h3>Ultra High red Backpack</h3>
  <p>Lorem ipsum dolor sit amet, consectetur adipiscing elitt. Maecenas eleifend metus...</p>
  <span class="price">€350.22</span><span class="stars"><b>★★</b>★★★</span>
  <span class="cart"><span class="ic"><svg width="9" height="8" viewBox="0 0 9 8"><path d="M0 1h2l1 4h5l1-3H3" fill="none" stroke="#fff" stroke-width="1"/><circle cx="3.5" cy="7" r=".8" fill="#fff"/><circle cx="7" cy="7" r=".8" fill="#fff"/></svg></span><span class="tx">add to cart</span></span>
  <span class="details">details</span>
  <div class="pimg" role="img" aria-label="Red trekking backpack"></div>
</article>

<section class="abs info">
  <div class="abs info-col" style="left:19px">
    <h2>BRAMBLETON EQUIPMENT</h2>
    <h4>Start your adventure here</h4>
    <p>Lorem ipsum dolor sit amet, consectetur adipiscing elit. Maecenas eleifend metus hendrerit, commodo massa eu, luctus ipsum. Vivamus at nisi ac metus con-sectetur fermentum eget vel quam.</p>
    <span class="more">read more</span>
    <div class="circle" style="background:radial-gradient(circle at 40% 35%,#ffffff,#e3e6ea)" role="img" aria-label="Brand emblem"></div>
  </div>
  <div class="abs info-col" style="left:344px">
    <h2>HIGH QUALITY MATERIALS</h2>
    <h4>Lorem ipsum dolor sit amet</h4>
    <p>Lorem ipsum dolor sit amet, consectetur adipiscing elit. Maecenas eleifend metus hendrerit, commodo massa eu, luctus ipsum. Vivamus at nisi ac metus con-sectetur fermentum eget vel quam.</p>
    <span class="more">read more</span>
    <div class="circle" style="background:radial-gradient(circle at 45% 40%,#ece8e0,#bdb8ae)" role="img" aria-label="Close-up of woven rope fabric"></div>
  </div>
</section>

<section class="abs news">
  <h3>Sign Up for Newsletter</h3>
  <p>If you sign up for our newsletter, you'll get exclusive right to get latest product updates info.</p>
  <span class="field">Your email address</span>
  <span class="submit">Submit</span>
</section>

<footer>
  <div class="abs foot-rule"></div>
  <div class="abs foot-square"></div>
  <div class="abs foot-col" style="left:58px"><h5>BRAMBLETON</h5><a>About Us</a><a>Stores</a><a>Online Shop</a><a>Contact</a></div>
  <div class="abs foot-col" style="left:162px"><h5>OUR PRODUCTS</h5><a>Backpacks</a><a>Clothing</a><a>Equipment</a><a>Catalogues</a></div>
  <div class="abs foot-col" style="left:276px"><h5>COMPANY</h5><a>Jobs ad Brambleton</a><a>Contact</a><a>Privacy Policy</a><a>FAQs</a></div>
  <div class="abs world" role="img" aria-label="Dotted world map"></div>
  <div class="abs foot-brand"><span class="brand-square"></span><span class="brand-name">BRAMBLETON</span></div>
</footer>
</body>
</html>
```